Autodetailing namecard design: Rose Gold Lettering on Black Matt

This is a namecard design project
requiring two-sided design
Base Color of Namecard: black matt

On front:
Company name,
"Lumen Finishes 47 Kelapa"
Subtext: Auto Detailing Studio

Name of card holder: Dennis Lowe
Phone Number: +6012-4837-5062
address: 47, Jalan Kelapa 3/5Taman Seri Kelapa, 81200 Johor Bahru, Johor, Malaysia

Back:
Our Services
High Gloss Car Paint Protection
Custom Color Modification and Styling
Anti-Chip Glass Protection Film
Heat Rejection Glass Tinting

Target Market(s)

Autodetailing for highend cars

Contact Information for Business Card

as mentioned in project details

Colors

Designer to choose colors to be used in the design.

Requirements
Must have
• The main value-add to this project is the design of a logo suited for our purpose and name, and the inclusion of business card details into the card design

```html
<!DOCTYPE html>
<html lang="en">
<head>
<meta charset="utf-8">
<title>Lumen Finishes 47 Kelapa – Business Card</title>
<link rel="stylesheet" href="https://fonts.googleapis.com/css2?family=Montserrat:wght@300;400;700&display=swap">
<style>
  :root {
    --canvas: #ececec;
    --card-dark: #232323;
    --card-light: #ffffff;
    --accent-red: #c8202a;
    --text-white: #ffffff;
    --text-dark: #2b2b2b;
    --label: #333333;
  }
  * { box-sizing: border-box; margin: 0; padding: 0; }
  html, body { width: 1200px; height: 796px; overflow: hidden; }
  body {
    background: var(--canvas);
    font-family: "Montserrat", Arial, sans-serif;
    position: relative;
  }
  .card {
    position: absolute;
    left: 330px;
    width: 540px;
    height: 324px;
    overflow: hidden;
    box-shadow: 0 2px 8px rgba(0,0,0,0.12);
  }
  .card-back { top: 14px; background: var(--card-dark); }
  .card-front { top: 424px; background: var(--card-light); }
  .side-label {
    position: absolute;
    left: 330px;
    width: 540px;
    text-align: center;
    font-weight: 700;
    font-size: 34px;
    color: var(--label);
    letter-spacing: 0.5px;
  }
  .label-back { top: 346px; }
  .label-front { top: 752px; }

  .car-visual {
    position: absolute;
    background: radial-gradient(ellipse at 50% 55%, rgba(70,70,70,0.55) 0%, rgba(45,45,45,0.35) 45%, rgba(35,35,35,0) 75%);
  }
  .card-back .car-visual { left: 40px; top: 110px; width: 460px; height: 170px; }
  .card-front .car-visual { left: 40px; top: 20px; width: 460px; height: 150px; }

  .brand-mark {
    position: absolute;
    left: 0; width: 100%;
    text-align: center;
    font-weight: 700;
    font-size: 7px;
    letter-spacing: 0.4px;
    text-transform: uppercase;
    color: var(--accent-red);
  }
  .brand-name {
    position: absolute;
    left: 0; width: 100%;
    text-align: center;
    font-weight: 700;
    color: var(--text-white);
    text-transform: uppercase;
  }
  .brand-sub {
    position: absolute;
    left: 0; width: 100%;
    text-align: center;
    font-weight: 300;
    color: var(--accent-red);
    text-transform: uppercase;
    letter-spacing: 0.6px;
  }

  /* back */
  .card-back .brand-mark { top: 70px; }
  .card-back .brand-name { top: 89px; font-size: 15.5px; }
  .card-back .brand-sub { top: 105px; font-size: 11.5px; }
  .card-back .divider {
    position: absolute; left: 88px; top: 123px; width: 360px; height: 2px;
    background: var(--accent-red);
  }
  .services-title {
    position: absolute; left: 0; width: 100%; top: 149px;
    text-align: center; font-weight: 700; font-size: 17px;
    color: var(--text-white); text-transform: uppercase;
  }
  .services-list { position: absolute; left: 0; width: 100%; top: 174px; list-style: none; }
  .services-list li {
    text-align: center; height: 19.7px; line-height: 19.7px;
    font-size: 13px; font-weight: 400; letter-spacing: 0.4px;
    color: var(--accent-red); text-transform: uppercase;
  }
  .services-list .chev { color: var(--text-white); margin: 0 6px; font-weight: 400; }

  /* front */
  .front-band { position: absolute; left: 0; top: 0; width: 100%; height: 162px; background: var(--card-dark); }
  .card-front .brand-mark { top: 76px; }
  .card-front .brand-name { top: 96px; font-size: 19px; }
  .card-front .brand-sub { top: 117px; font-size: 15px; }
  .holder-name {
    position: absolute; left: 84px; top: 209px;
    font-size: 22px; color: var(--text-dark); text-transform: uppercase;
  }
  .holder-name .first { font-weight: 700; }
  .holder-name .last { font-weight: 300; color: var(--accent-red); }
  .contact-divider {
    position: absolute; left: 272px; top: 178px; width: 2px; height: 94px;
    background: var(--accent-red);
  }
  .contact-address {
    position: absolute; left: 306px; top: 189px; width: 200px;
    font-style: normal; font-size: 11.5px; line-height: 14px; color: var(--text-dark);
  }
  .contact-phone {
    position: absolute; left: 304px; top: 243px;
    font-size: 13px; color: var(--text-dark); letter-spacing: 0.3px;
  }
</style>
</head>
<body>

<section class="card card-back" aria-label="Business card back">
  <div class="car-visual" role="img" aria-label="Faint photograph of a dark luxury sports car"></div>
  <div class="brand-mark">Lumen Finishes 47 Kelapa</div>
  <div class="brand-name">Lumen Finishes 47 Kelapa</div>
  <div class="brand-sub">Auto Detailing Studio</div>
  <div class="divider"></div>
  <h2 class="services-title">Our Services</h2>
  <ul class="services-list">
    <li><span class="chev">»</span>High Gloss Car Paint Protection<span class="chev">«</span></li>
    <li><span class="chev">»</span>Custom Color Modification and Styling<span class="chev">«</span></li>
    <li><span class="chev">»</span>Anti-Chip Glass Protection Film<span class="chev">«</span></li>
    <li><span class="chev">»</span>Heat Rejection Glass Tinting<span class="chev">«</span></li>
  </ul>
</section>
<div class="side-label label-back">BACK</div>

<section class="card card-front" aria-label="Business card front">
  <div class="front-band"></div>
  <div class="car-visual" role="img" aria-label="Faint photograph of a dark luxury sports car"></div>
  <div class="brand-mark">Lumen Finishes 47 Kelapa</div>
  <div class="brand-name">Lumen Finishes 47 Kelapa</div>
  <div class="brand-sub">Auto Detailing Studio</div>
  <div class="holder-name"><span class="first">Dennis</span> <span class="last">Lowe</span></div>
  <div class="contact-divider"></div>
  <address class="contact-address">47, Jalan Kelapa 3/5 Taman Seri Kelapa, 81200 Johor Bahru, Johor, Malaysia</address>
  <div class="contact-phone">+6012-4837-5062</div>
</section>
<div class="side-label label-front">FRONT</div>

</body>
</html>
```